Webdesign für Entrümpelungsfirma
Zielgruppe
Unsere Firma heißt Tolu Hausservice und wir bieten folgende Dienstleistungen an:
Haushaltsauflösungen, Entrümpelungen, Messie-Wohnungen, Demontage-Arbeiten, Gartenpflege.
Aufgabenstellung
Unsere jetzige Seite: www.hausservice-fernwald.example
Das Logo bleibt bestehen. Es wäre schön, wenn das neue Design die Farben aufnehmen würde. Es geht erstmal nur um die Startseite.
Die Struktur soll klar und übersichtlich sein.
Wir möchten Vertrauen erwecken, aber nicht langweilig wirken. Das Design soll pfiffig sein und den Kunden aufmerksam machen.
Eine Seite, die uns sehr gut gefällt:
http://www.saubermoni.example/

```html
<!DOCTYPE html>
<html lang="de">
<head>
<meta charset="utf-8">
<title>Tolu Hausservice – Startseite mobil</title>
<link rel="stylesheet" href="https://fonts.googleapis.com/css2?family=Open+Sans:wght@300;400;600;700&display=swap">
<style>
  :root {
    --stage: #eceef0;
    --page: #ffffff;
    --olive: #8c9e1a;
    --lime: #a9c22a;
    --sun: #f2c418;
    --navy: #1d4f9c;
    --text: #555555;
    --banner-light: #f6ead6;
    --banner-dark: #e6cfae;
    --furniture: #c9a987;
    --sky-light: #e3f6fa;
    --sky: #a9e0ec;
  }
  * { box-sizing: border-box; margin: 0; padding: 0; }
  html, body {
    width: 1130px; height: 1200px; overflow: hidden;
    background: var(--stage);
    font-family: "Open Sans", Arial, sans-serif;
  }
  .page {
    position: absolute; left: 233px; top: 14px;
    width: 664px; height: 1172px; overflow: hidden;
    background: var(--page);
  }
  .topbar {
    height: 107px; background: var(--olive);
    border-bottom: 6px solid var(--sun);
    display: flex; align-items: center; justify-content: center; gap: 34px;
    color: #fff; font-weight: 700; font-size: 25px; white-space: nowrap;
  }
  .topbar a { color: inherit; text-decoration: none; display: flex; align-items: center; gap: 8px; }
  .topbar svg { width: 24px; height: 24px; fill: #fff; }
  .header { position: relative; height: 266px; }
  .menu-toggle {
    position: absolute; left: 32px; top: 113px; width: 42px;
    display: flex; flex-direction: column; gap: 8px;
  }
  .menu-toggle span { display: block; height: 6px; border-radius: 3px; background: var(--navy); }
  .brand {
    position: absolute; left: 0; right: 0; top: 112px;
    display: flex; align-items: center; justify-content: center; gap: 14px;
  }
  .brand-dot { width: 34px; height: 34px; border-radius: 50%; background: var(--sun); }
  .brand-name { font-weight: 700; font-size: 34px; color: var(--navy); line-height: 1; }

  .hero-banner {
    position: relative;
    margin: 13px 16px 0; height: 211px; overflow: hidden;
    background: linear-gradient(90deg, var(--banner-dark), var(--banner-light) 50%, var(--banner-dark));
    box-shadow: 0 8px 10px -6px rgba(0,0,0,0.18);
  }
  .hero-photo {
    position: absolute; left: 60px; right: 110px; top: 60px; height: 130px;
    background: linear-gradient(180deg, rgba(201,169,135,0) 0%, rgba(201,169,135,0.55) 100%);
    border-radius: 8px;
  }
  .badge {
    position: absolute; border-radius: 50%;
    display: flex; flex-direction: column; align-items: center; justify-content: center;
    text-align: center; color: #fff; font-weight: 700; line-height: 1.15;
  }
  .badge-main { left: 104px; top: 34px; width: 112px; height: 112px; background: var(--navy); }
  .badge-main small { font-size: 9px; font-weight: 600; margin-bottom: 4px; }
  .badge-main span { font-size: 17px; }
  .badge-guarantee { left: 293px; top: 29px; width: 90px; height: 90px; background: var(--olive); font-size: 9px; }
  .badge-visit { left: 231px; top: 131px; width: 70px; height: 70px; background: var(--sun); font-size: 8px; }
  .badge-fast { left: 441px; top: 43px; width: 106px; height: 106px; background: var(--lime); font-size: 16px; }

  .intro { text-align: center; padding-top: 136px; }
  .intro h1 { font-weight: 400; font-size: 42px; color: var(--text); line-height: 1.1; }
  .intro .rule { width: 80px; height: 5px; background: var(--sun); margin: 28px auto 34px; }
  .intro p { font-size: 29px; line-height: 1.32; color: var(--text); }
  .service-visual {
    position: absolute; left: 32px; top: 1010px; width: 600px; height: 600px;
    border-radius: 50%;
    background: radial-gradient(circle at 50% 40%, var(--sky-light), var(--sky));
  }
</style>
</head>
<body>
  <main class="page">
    <div class="topbar">
      <a href="#angebot">
        <svg viewBox="0 0 24 24" aria-hidden="true"><path d="M4 11h11.2l-4.6-4.6L12 5l7 7-7 7-1.4-1.4 4.6-4.6H4z"/></svg>
        Angebot anfordern
      </a>
      <a href="tel:070005550123">
        <svg viewBox="0 0 24 24" aria-hidden="true"><path d="M6.6 10.8a15.1 15.1 0 0 0 6.6 6.6l2.2-2.2c.3-.3.7-.4 1-.2 1.1.4 2.3.6 3.6.6.6 0 1 .4 1 1V20c0 .6-.4 1-1 1A17 17 0 0 1 3 4c0-.6.4-1 1-1h3.5c.6 0 1 .4 1 1 0 1.3.2 2.5.6 3.6.1.3 0 .7-.2 1z"/></svg>
        Hotline: 07000 5550123
      </a>
    </div>

    <header class="header">
      <div class="menu-toggle" aria-label="Menü"><span></span><span></span><span></span></div>
      <div class="brand">
        <div class="brand-dot"></div>
        <div class="brand-name">Tolu Hausservice</div>
      </div>
    </header>

    <section class="hero-banner">
      <div class="hero-photo" role="img" aria-label="Alte Möbel, Fahrrad, Fernseher, rotes Sofa und Waschmaschine"></div>
      <div class="badge badge-main"><small>Tolu Hausservice</small><span>Wir<br>entrümpeln</span></div>
      <div class="badge badge-guarantee">100%<br>Zufriedenheits-<br>garantie</div>
      <div class="badge badge-visit">Gratis<br>Besichtigung</div>
      <div class="badge badge-fast">alles<br>schnell<br>erledigt</div>
    </section>

    <section class="intro">
      <h1>Allround-Service</h1>
      <div class="rule"></div>
      <p>Wir bieten Ihnen einen Rundum-Service<br>für Ihre Liegenschaft an:</p>
    </section>

    <div class="service-visual" role="img" aria-label="Illustration mit Werkzeugen wie Heckenschere, Schraubenschlüssel und Sackkarre"></div>
  </main>
</body>
</html>
```